Real Estate Sales Brokerage

Design a modern and fresh looking standard size business card, incorporate our logo's color scheme and modern appearance with head shot photo on front side and incorporate our log on the back side

Target Market(s)

Residential Home sales

Industry/Entity Type

Real Estate Agent

Font styles to use
Sans Serif

Colors

Designer to choose colors to be used in the design.

Requirements
Must have
• fresh, modern, not too busy, incorporate head shot in front of the card, incorporate logo in front and back of the card. Use logo design scheme as appropriate.
Nice to have
• horizontal and vertical options to compare would be nice.

```html
<!DOCTYPE html>
<html lang="en">
<head>
<meta charset="utf-8">
<title>Keystone Harbor Realty – Business Card</title>
<link href="https://fonts.googleapis.com/css2?family=Roboto:wght@400;500;700&display=swap" rel="stylesheet">
<style>
  :root {
    --olive: #5e5b31;
    --yellow: #f5d03f;
    --white: #ffffff;
    --stage: #3a3431;
    --photo-top: #c9b98f;
    --photo-bottom: #2d4a86;
  }
  * { margin: 0; padding: 0; box-sizing: border-box; }
  html, body { width: 1200px; height: 780px; overflow: hidden; }
  body {
    background: var(--stage);
    font-family: "Roboto", Arial, sans-serif;
    position: relative;
  }
  .card {
    position: absolute;
    top: 235px;
    width: 540px;
    height: 310px;
    border-radius: 16px;
    overflow: hidden;
    background: var(--white);
    box-shadow: 0 10px 28px rgba(0,0,0,.45);
  }
  .card--front { left: 40px; }
  .card--back { left: 620px; }
  .card__shapes { position: absolute; inset: 0; }
  .headshot {
    position: absolute;
    left: 300px; top: 20px;
    width: 240px; height: 290px;
    background: linear-gradient(180deg, var(--photo-top) 0%, #8a8ea8 45%, var(--photo-bottom) 100%);
  }
  .brand {
    position: absolute;
    display: flex;
    align-items: center;
    gap: 12px;
  }
  .brand__mark {
    width: 46px; height: 46px;
    background: var(--olive);
  }
  .brand__name {
    color: var(--olive);
    font-weight: 700;
    font-size: 20px;
    line-height: 1.05;
    letter-spacing: .5px;
    text-transform: uppercase;
  }
  .card--front .brand { left: 34px; top: 40px; }
  .card--back .brand { left: 150px; top: 90px; }
  .card--back .brand__mark { width: 56px; height: 56px; }
  .card--back .brand__name { font-size: 24px; }
  .agent {
    position: absolute;
    left: 30px; top: 178px;
    color: var(--white);
  }
  .agent__name { font-size: 19px; font-weight: 700; letter-spacing: .3px; }
  .agent__title { font-size: 11px; font-weight: 700; color: var(--yellow); margin-top: 1px; letter-spacing: .4px; }
  .agent__address { font-size: 11.5px; line-height: 1.35; margin-top: 5px; }
  .contact { list-style: none; margin-top: 6px; font-size: 11.5px; }
  .contact li { display: flex; align-items: center; gap: 7px; line-height: 1.45; }
  .contact svg { width: 12px; height: 12px; flex: none; }
  .back-address {
    position: absolute;
    left: 0; right: 0; top: 247px;
    text-align: center;
    color: var(--white);
    font-size: 11.5px;
    letter-spacing: .3px;
  }
</style>
</head>
<body>

<section class="card card--front" aria-label="Business card front">
  <svg class="card__shapes" viewBox="0 0 540 310" aria-hidden="true">
    <polygon points="250,0 540,0 540,210" fill="var(--yellow)"/>
    <polygon points="0,172 300,108 300,310 0,310" fill="var(--olive)"/>
    <polygon points="0,270 0,310 52,310" fill="var(--yellow)"/>
  </svg>
  <div class="headshot" role="img" aria-label="Head shot photo of the managing director in a navy suit"></div>

  <div class="brand">
    <span class="brand__mark"></span>
    <span class="brand__name">Keystone<br>Harbor<br>Realty</span>
  </div>

  <div class="agent">
    <p class="agent__name">DANIEL MARSH</p>
    <p class="agent__title">MANAGING DIRECTOR</p>
    <p class="agent__address">410 W. Larkspur Ave<br>Suite 220, P.O. Box 18452</p>
    <ul class="contact">
      <li>
        <svg viewBox="0 0 12 12"><rect width="12" height="12" rx="2" fill="var(--yellow)"/><rect x="4" y="2" width="4" height="8" rx="1" fill="none" stroke="var(--olive)" stroke-width="1.2"/></svg>
        555.204.6318
      </li>
      <li>
        <svg viewBox="0 0 12 12"><rect width="12" height="12" rx="2" fill="var(--yellow)"/><rect x="2.5" y="3.5" width="7" height="5" fill="none" stroke="var(--olive)" stroke-width="1"/><path d="M2.5 3.5 L6 6.5 L9.5 3.5" fill="none" stroke="var(--olive)" stroke-width="1"/></svg>
        daniel@keystoneharborrealty.com
      </li>
      <li>
        <svg viewBox="0 0 12 12"><rect width="12" height="12" rx="2" fill="var(--yellow)"/><circle cx="6" cy="6" r="3.5" fill="none" stroke="var(--olive)" stroke-width="1"/><path d="M2.5 6 H9.5 M6 2.5 V9.5" stroke="var(--olive)" stroke-width=".8"/></svg>
        www.keystoneharborrealty.com
      </li>
    </ul>
  </div>
</section>

<section class="card card--back" aria-label="Business card back">
  <svg class="card__shapes" viewBox="0 0 540 310" aria-hidden="true">
    <polygon points="0,240 540,240 540,275 0,275" fill="var(--olive)"/>
    <polygon points="440,240 540,215 540,240" fill="var(--yellow)"/>
  </svg>
  <div class="brand">
    <span class="brand__mark"></span>
    <span class="brand__name">Keystone<br>Harbor<br>Realty</span>
  </div>
  <p class="back-address">410 W. Larkspur Ave, Suite 220, P.O. Box 18452</p>
</section>

</body>
</html>
```